Packing for Disinfectant wipes

Design the Packinging for new Disinfectant wipes. Wipes are for cleaning and disinfectanting hard surfaces and equipment. There are 100 wipes to the packet (size 230mm x 300mm). The company is called Norbeck Supplies and is supplier of consumable products to healthcare companies. Wipes are not for use on humans/baby. Packaging size as per attachment.
Industry/Entity Type
Healthcare
Requirements
Nice to have
- Packaging need ingredients list and directions for use

```html
<!DOCTYPE html>
<html lang="en">
<head>
<meta charset="utf-8">
<title>Norbeck Supplies Disinfectant Wipes Pack</title>
<link href="https://fonts.googleapis.com/css2?family=Montserrat:ital,wght@0,500;0,700;1,800&family=Poppins:wght@400;700&display=swap" rel="stylesheet">
<style>
  :root{
    --paper:#ffffff;
    --pack-white:#eeeeea;
    --ink:#2b3a44;
    --green:#2f7d16;
    --lime:#8aad1a;
    --blue:#0f3f8c;
    --sky:#4f9fd0;
    --orange:#e8641a;
    --amber:#e59436;
    --lid-edge:#f4f6f5;
    --band:#ee6a14;
  }
  html,body{margin:0;padding:0;width:1200px;height:733px;overflow:hidden;background:var(--paper);}
  .canvas{position:relative;width:1200px;height:733px;}
  .pack-art{position:absolute;left:0;top:0;}
  .pack-count{
    position:absolute;left:272px;top:152px;margin:0;
    font-family:"Poppins",sans-serif;color:var(--ink);line-height:1;
  }
  .pack-count .count{display:block;font-weight:700;font-size:26px;}
  .pack-count .kind{display:block;font-weight:400;font-size:20px;margin-top:2px;}
  .usage-note{
    position:absolute;left:196px;top:512px;transform-origin:0 0;transform:rotate(-90deg);
    font-family:"Poppins",sans-serif;font-style:italic;font-size:6.5px;line-height:1.35;color:var(--ink);
    white-space:nowrap;margin:0;
  }
  .lid{position:absolute;left:393px;top:228px;width:360px;height:202px;}
  .brand{
    position:absolute;left:0;top:282px;width:1146px;display:flex;justify-content:center;align-items:center;gap:6px;
    font-family:"Montserrat",sans-serif;font-weight:500;font-size:15px;color:var(--ink);
  }
  .brand .mark{width:11px;height:11px;background:var(--lime);display:inline-block;}
  .product-name{
    position:absolute;left:423px;top:316px;width:312px;margin:0;text-align:center;
    font-family:"Montserrat",sans-serif;font-style:italic;font-weight:800;font-size:49px;
    letter-spacing:-1px;color:var(--ink);line-height:1;
    text-shadow:1.5px 0 0 #fff,-1.5px 0 0 #fff,0 1.5px 0 #fff,0 -1.5px 0 #fff,
                1px 1px 0 #fff,-1px -1px 0 #fff,1px -1px 0 #fff,-1px 1px 0 #fff;
  }
  .product-band{
    position:absolute;left:436px;top:367px;width:294px;height:29px;
    background:linear-gradient(90deg,rgba(238,106,20,0) 0%,var(--band) 15%,var(--band) 85%,rgba(238,106,20,0) 100%);
    display:flex;align-items:center;justify-content:center;
    font-family:"Montserrat",sans-serif;font-weight:700;font-size:21px;color:#ffffff;letter-spacing:.5px;
  }
</style>
</head>
<body>
<div class="canvas">
  <svg class="pack-art" width="1200" height="733" viewBox="0 0 1200 733">
    <defs>
      <linearGradient id="colour-sweep" x1="0" y1="0" x2="1" y2="0">
        <stop offset="0" stop-color="var(--green)"/>
        <stop offset="0.22" stop-color="var(--lime)"/>
        <stop offset="0.45" stop-color="var(--sky)"/>
        <stop offset="0.62" stop-color="#c98a4a"/>
        <stop offset="0.78" stop-color="var(--orange)"/>
        <stop offset="1" stop-color="var(--amber)"/>
      </linearGradient>
      <linearGradient id="top-shade" x1="0" y1="0" x2="0" y2="1">
        <stop offset="0" stop-color="var(--blue)" stop-opacity="0.85"/>
        <stop offset="0.5" stop-color="var(--blue)" stop-opacity="0"/>
      </linearGradient>
      <radialGradient id="blue-fade" cx="0.3" cy="0" r="0.7">
        <stop offset="0" stop-color="#fff" stop-opacity="1"/>
        <stop offset="1" stop-color="#fff" stop-opacity="0"/>
      </radialGradient>
      <mask id="shade-mask"><rect x="560" y="118" width="320" height="300" fill="url(#blue-fade)"/></mask>
      <radialGradient id="swirl-glow" cx="0.5" cy="0.5" r="0.5">
        <stop offset="0" stop-color="#ffffff" stop-opacity="0.5"/>
        <stop offset="0.6" stop-color="#f6d2b0" stop-opacity="0.3"/>
        <stop offset="1" stop-color="#f6d2b0" stop-opacity="0"/>
      </radialGradient>
      <clipPath id="colour-clip">
        <path d="M632 118 L1045 118 L1115 600 L1030 640 L250 640 C240 520 250 420 320 330 C400 230 560 210 632 118 Z"/>
      </clipPath>
    </defs>
    <path class="pack-body" d="M128 118 L640 118 L640 640 L130 640 L120 560 L40 565 L120 520 Z" fill="var(--pack-white)"/>
    <g clip-path="url(#colour-clip)">
      <rect class="colour-area" x="240" y="118" width="880" height="522" fill="url(#colour-sweep)"/>
      <rect x="560" y="118" width="320" height="300" fill="url(#top-shade)" mask="url(#shade-mask)"/>
      <ellipse role="img" aria-label="Decorative swirl and bubble pattern" cx="905" cy="380" rx="200" ry="190" fill="url(#swirl-glow)"/>
    </g>
  </svg>

  <p class="pack-count"><span class="count">100 wipes</span><span class="kind">disinfectant</span></p>
  <p class="usage-note">For cleaning and disinfectanting hard surfaces and equipment.<br>Not for use on humans.</p>

  <svg class="lid" viewBox="0 0 360 202" width="360" height="202">
    <path d="M28 3 H332 Q356 3 356 27 V172 Q356 194 332 194 H28 Q4 194 4 172 V27 Q4 3 28 3 Z" fill="rgba(255,255,255,0.18)" stroke="var(--lid-edge)" stroke-width="4"/>
    <path d="M150 194 Q180 210 210 194" fill="rgba(255,255,255,0.35)"/>
  </svg>
  <div class="brand"><span class="mark"></span>Norbeck Supplies</div>
  <h1 class="product-name">Disinfectant</h1>
  <div class="product-band">WIPES</div>
</div>
</body>
</html>
```